Design a compelling Tarnwell Business Card that will drive people to my site

I want a business card that I can give to people—less to tell them who I am and more to direct them to my website. My website is a portal for Crestlane Aquatics Officials and a place for people who want to become Crestlane Aquatics Officials.
I am uploading my official company logo as well as a business card mockup that I did on my own. Please feel free to completely stray from this design.
I've included a screen recording of the homepage of my website as well.
Target Market(s)
Crestlane Aquatics Officials and people who desire to become one
Contact Information for Business Card
website url
Look and feel
Each slider illustrates characteristics of the customer's brand and the style your logo design should communicate.

```html
<!DOCTYPE html>
<html lang="en">
<head>
<meta charset="utf-8">
<title>Tarnwell Business Card</title>
<link href="https://fonts.googleapis.com/css2?family=Arimo:wght@400;700&display=swap" rel="stylesheet">
<style>
  :root {
    --page-bg: #2b2b2d;
    --card-white: #f7f7f8;
    --card-shade: #e6e6e8;
    --brand-blue: #354f9e;
    --brand-deep: #2f44a0;
    --brand-light: #8fa4d6;
    --text-grey: #555a66;
    --text-white: #ffffff;
  }
  * { box-sizing: border-box; margin: 0; padding: 0; }
  html, body { width: 1200px; height: 900px; overflow: hidden; }
  body {
    background: var(--page-bg);
    font-family: "Arimo", Arial, sans-serif;
    position: relative;
  }
  .card {
    position: absolute;
    left: 320px;
    width: 560px;
    height: 320px;
    overflow: hidden;
    background: linear-gradient(100deg, var(--card-shade) 0%, var(--card-white) 45%, #ffffff 100%);
    box-shadow: 0 12px 30px rgba(0,0,0,0.45);
  }
  .card--front { top: 100px; }
  .card--back { top: 480px; }

  .wordmark {
    display: flex;
    align-items: center;
    gap: 12px;
    color: var(--brand-deep);
    font-weight: 700;
    font-size: 54px;
    letter-spacing: -1px;
    line-height: 1;
  }
  .wordmark__dot {
    width: 22px;
    height: 22px;
    border-radius: 50%;
    background: var(--brand-light);
    flex: none;
  }
  .card--front .wordmark {
    position: absolute;
    left: 0; right: 0;
    top: 118px;
    justify-content: center;
  }
  .site-url {
    position: absolute;
    left: 0; right: 0;
    top: 186px;
    text-align: center;
    font-size: 15px;
    color: var(--text-grey);
  }

  .back-wave { position: absolute; inset: 0; }
  .card--back .wordmark {
    position: absolute;
    left: 300px;
    top: 80px;
    font-size: 48px;
  }
  .contact {
    position: absolute;
    left: 34px;
    bottom: 40px;
    color: var(--text-white);
  }
  .contact__name {
    font-size: 19px;
    font-weight: 700;
    color: var(--brand-light);
  }
  .contact__role { font-size: 16px; margin-top: 4px; }
  .contact__list { list-style: none; margin-top: 20px; }
  .contact__item {
    display: flex;
    align-items: center;
    gap: 8px;
    font-size: 15px;
    margin-top: 6px;
  }
  .contact__icon { width: 15px; height: 15px; flex: none; }
</style>
</head>
<body>
  <section class="card card--front" aria-label="Card front">
    <div class="wordmark"><span class="wordmark__dot"></span>Tarnwell</div>
    <p class="site-url">www.tarnwell.com</p>
  </section>

  <section class="card card--back" aria-label="Card back">
    <svg class="back-wave" viewBox="0 0 560 320" preserveAspectRatio="none" aria-hidden="true">
      <path d="M0 0 H262 C226 40 240 110 300 170 C350 220 380 270 398 320 H0 Z" fill="var(--brand-light)"/>
      <path d="M0 0 H246 C212 42 226 112 286 174 C334 222 362 272 380 320 H0 Z" fill="#6f86c6"/>
      <path d="M0 0 H232 C198 44 212 114 272 178 C318 226 346 274 364 320 H0 Z" fill="var(--brand-blue)"/>
    </svg>
    <div class="wordmark"><span class="wordmark__dot"></span>Tarnwell</div>
    <div class="contact">
      <p class="contact__name">Daniel Marrow</p>
      <p class="contact__role">CEO &amp; Founder</p>
      <ul class="contact__list">
        <li class="contact__item">
          <svg class="contact__icon" viewBox="0 0 24 24" aria-hidden="true"><path fill="#fff" d="M6.6 10.8a15.1 15.1 0 0 0 6.6 6.6l2.2-2.2a1 1 0 0 1 1-.25 11.4 11.4 0 0 0 3.6.57 1 1 0 0 1 1 1V20a1 1 0 0 1-1 1A17 17 0 0 1 3 4a1 1 0 0 1 1-1h3.5a1 1 0 0 1 1 1c0 1.25.2 2.45.57 3.6a1 1 0 0 1-.25 1z"/></svg>
          (404) 555-0172
        </li>
        <li class="contact__item">
          <svg class="contact__icon" viewBox="0 0 24 24" aria-hidden="true"><path fill="#fff" d="M2 5h20v14H2z M4 7v.5l8 5 8-5V7z" fill-rule="evenodd"/></svg>
          dan@tarnwell.com
        </li>
      </ul>
    </div>
  </section>
</body>
</html>
```